Clinicians Prime Bold "NOT YOUR DADDY's CARD" clear Card make the card you always wanted

I need a stand out business card, I would like it to be crazy modern using a
clear plastic 30 mil card, let this be your PHD thesis in Card Design, make it fun and cutting edge. Make it Toxicology Lab meets Night Club. Colors are tans and browns with a hint of gold, because we test PEE (urine) and we call it Liquid Gold!!

Target Market(s)

it goes to Dr. Offices, but I want them to say wow Nice card, and I want our Salesmen to say" We are not your Fathers Lab" we are NEW BOLD and Different....

Industry/Entity Type

Plastic

Contact Information for Business Card

Clinician's Prime Toxicology 2873 Fernhollow Avenue SE | Atlanta, GA 30472
Phone: 404.555.0173 | Fax: 404.555.0174 my cell phone 404.555.0198 my email is Lionel@cliniciansprimetoxicology.example

CLIA#47K9315062 | Lionel Ashcombe, CEO, GED
www.cliniciansprimetoxicology.example

Requirements
Must have
• Clear Card design, I want it to be double sided, unless you can show me a design that can only need one side because it is that GOOD
Should not have
• Should not look like a conservative lab

```html
<!DOCTYPE html>
<html lang="en">
<head>
<meta charset="utf-8">
<title>Clinician's Prime Toxicology – Clear Business Card</title>
<link href="https://fonts.googleapis.com/css2?family=Questrial&family=Open+Sans:wdth,wght@75..100,300..600&display=swap" rel="stylesheet">
<style>
  :root {
    --backdrop: #a9a7a3;
    --clear-top: rgba(255, 255, 255, 0.42);
    --clear-bottom: rgba(255, 255, 255, 0.26);
    --clear-edge: rgba(255, 255, 255, 0.7);
    --orange: #f5821f;
    --band-grey: #b3b3b3;
    --ink: #1e1e1e;
    --muted: #7d7d7d;
    --brand: #8a6a4f;
    --gold: #c79a5a;
    --white: #ffffff;
  }
  * { box-sizing: border-box; margin: 0; padding: 0; }
  html, body { width: 1200px; height: 1000px; overflow: hidden; }
  body { background: var(--backdrop); font-family: "Questrial", sans-serif; color: var(--ink); position: relative; }

  .card {
    position: absolute; left: 210px; width: 780px;
    background: linear-gradient(160deg, var(--clear-top) 0%, var(--clear-bottom) 55%, var(--clear-top) 100%);
    border: 1px solid var(--clear-edge);
    border-radius: 24px; overflow: hidden;
    box-shadow: inset 0 1px 0 rgba(255,255,255,0.8), 0 6px 18px rgba(0,0,0,0.12);
  }
  .card--front { top: 47px; height: 443px; }
  .card--back { top: 508px; height: 445px; }

  .abs { position: absolute; white-space: nowrap; }

  .brand { left: 28px; top: 62px; display: flex; align-items: center; gap: 22px; }
  .brand__dot { width: 54px; height: 54px; border-radius: 50%; background: var(--gold); flex: none; }
  .brand__name { color: var(--brand); font-size: 31px; line-height: 1.45; }

  .person { left: 482px; top: 92px; }
  .person__name { font-size: 22px; letter-spacing: 0.5px; }
  .person__title { font-size: 17px; color: var(--muted); margin-top: 9px; letter-spacing: 0.5px; }

  .tagline { left: 0; width: 100%; top: 228px; text-align: center; font-size: 22px; letter-spacing: 0.6px; }

  .stripe-orange { left: 0; width: 100%; height: 9px; background: var(--orange); }
  .stripe-grey { left: 0; width: 100%; height: 10px; background: var(--band-grey); }
  .panel { left: 0; width: 100%; background: var(--orange); color: var(--white); }

  .card--front .stripe-orange { top: 265px; }
  .card--front .stripe-grey { top: 275px; }
  .card--front .panel { top: 287px; bottom: 0; }

  .contact-row { position: absolute; top: 19px; left: 0; width: 100%; display: flex; justify-content: center; gap: 46px; }
  .contact { display: flex; align-items: center; gap: 12px; font-size: 33px; }
  .contact__icon { width: 46px; height: 46px; border-radius: 50%; background: var(--white); display: flex; align-items: center; justify-content: center; }
  .address { position: absolute; top: 83px; width: 100%; text-align: center; font-size: 21px; letter-spacing: 0.4px; }
  .web { position: absolute; top: 114px; width: 100%; text-align: center; font-size: 21px; letter-spacing: 0.4px; }

  .show-through { position: absolute; left: 0; top: 0; width: 780px; height: 265px; transform: scaleX(-1); opacity: 0.72; }
  .show-through .brand { top: 22px; opacity: 0.75; }
  .show-through .person { top: 96px; }
  .show-through .tagline { top: 232px; }

  .card--back .stripe-orange { top: 266px; }
  .card--back .stripe-grey { top: 277px; }
  .card--back .panel { top: 289px; bottom: 0; font-family: "Open Sans", sans-serif; }

  .what-we-do { position: absolute; top: 16px; width: 100%; text-align: center; font-size: 21px; }
  .what-we-do strong { font-weight: 600; }

  .services { position: absolute; top: 60px; left: 34px; display: flex; gap: 22px; }
  .service { display: flex; align-items: flex-start; gap: 12px; width: 216px; }
  .service__icon { width: 66px; height: 66px; border-radius: 50%; background: var(--white); flex: none; display: flex; align-items: center; justify-content: center; }
  .service__name { font-size: 22px; margin-top: 9px; }
  .service__note { font-weight: 400; font-stretch: 75%; font-size: 15px; margin-top: 0; }
</style>
</head>
<body>

<section class="card card--front">
  <div class="abs brand">
    <span class="brand__dot"></span>
    <span class="brand__name">Clinician's Prime<br>Toxicology</span>
  </div>
  <div class="abs person">
    <p class="person__name">Lionel Ashcombe</p>
    <p class="person__title">CEO, GED</p>
  </div>
  <p class="abs tagline">When it’s More Than “JUST&nbsp; RESULTS”</p>

  <div class="abs stripe-orange"></div>
  <div class="abs stripe-grey"></div>
  <div class="abs panel">
    <div class="contact-row">
      <span class="contact">
        <span class="contact__icon">
          <svg width="26" height="26" viewBox="0 0 24 24"><path fill="#f5821f" d="M6.6 10.8a15.1 15.1 0 0 0 6.6 6.6l2.2-2.2c.3-.3.7-.4 1-.2 1.1.4 2.3.6 3.6.6.6 0 1 .4 1 1V20c0 .6-.4 1-1 1A17 17 0 0 1 3 4c0-.6.4-1 1-1h3.5c.6 0 1 .4 1 1 0 1.3.2 2.5.6 3.6.1.3 0 .7-.2 1z"/></svg>
        </span>404.555.0173
      </span>
      <span class="contact">
        <span class="contact__icon">
          <svg width="24" height="26" viewBox="0 0 24 26"><rect x="3" y="8" width="18" height="16" rx="2" fill="#f5821f"/><rect x="7" y="2" width="10" height="8" fill="#f5821f"/><rect x="8.5" y="3.5" width="7" height="5" fill="#fff"/><g fill="#fff"><rect x="6" y="14" width="3" height="2"/><rect x="10.5" y="14" width="3" height="2"/><rect x="15" y="14" width="3" height="2"/><rect x="6" y="18" width="3" height="2"/><rect x="10.5" y="18" width="3" height="2"/><rect x="15" y="18" width="3" height="2"/></g></svg>
        </span>404.555.0174
      </span>
    </div>
    <p class="address">2873 Fernhollow Avenue SE, Atlanta, GA 30472</p>
    <p class="web">www.cliniciansprimetoxicology.example</p>
  </div>
</section>

<section class="card card--back">
  <div class="show-through" aria-hidden="true">
    <div class="abs brand">
      <span class="brand__dot"></span>
      <span class="brand__name">Clinician's Prime<br>Toxicology</span>
    </div>
    <div class="abs person">
      <p class="person__name">Lionel Ashcombe</p>
      <p class="person__title">CEO, GED</p>
    </div>
    <p class="abs tagline">When it’s More Than “JUST&nbsp; RESULTS”</p>
  </div>

  <div class="abs stripe-orange"></div>
  <div class="abs stripe-grey"></div>
  <div class="abs panel">
    <p class="what-we-do"><strong>What We Do:</strong> We get the testing done efficiently and accurately</p>
    <div class="services">
      <div class="service">
        <span class="service__icon">
          <svg width="26" height="36" viewBox="0 0 26 36"><path fill="#f5821f" d="M13 1C10 9 2 16 2 24a11 11 0 0 0 22 0C24 16 16 9 13 1z"/><path fill="#fff" d="M8 22c0 4 1.5 7 4 8-3.5 0-6-3-6-6.5z"/></svg>
        </span>
        <div><p class="service__name">Urine Testing</p><p class="service__note">check for substance use</p></div>
      </div>
      <div class="service">
        <span class="service__icon">
          <svg width="34" height="30" viewBox="0 0 34 30"><path fill="#f5821f" d="M17 29 3.5 16A8.5 8.5 0 0 1 17 5.2 8.5 8.5 0 0 1 30.5 16z"/></svg>
        </span>
        <div><p class="service__name">Rapid Results</p><p class="service__note">72 Hour turn-around</p></div>
      </div>
      <div class="service">
        <span class="service__icon">
          <svg width="24" height="40" viewBox="0 0 24 40"><g fill="none" stroke="#f5821f" stroke-width="2.4"><path d="M5 2c0 10 14 10 14 18S5 28 5 38"/><path d="M19 2c0 10-14 10-14 18s14 8 14 18"/></g><g stroke="#f5821f" stroke-width="2"><line x1="7" y1="6" x2="17" y2="6"/><line x1="9" y1="10" x2="15" y2="10"/><line x1="9" y1="30" x2="15" y2="30"/><line x1="7" y1="34" x2="17" y2="34"/></g></svg>
        </span>
        <div><p class="service__name">Genetic Testing</p></div>
      </div>
    </div>
  </div>
</section>

</body>
</html>
```